Ciel doux

Hello,
I’m a designer sunglasses reatail Store owner in Montreal, Quebec.

Looking for something modern, fresh with a trendy appeal.

Will send my logo.
Thank you.

Store

```html
<!DOCTYPE html>
<html lang="fr">
<head>
<meta charset="utf-8">
<title>Ciel doux — cartes d'affaires</title>
<link rel="stylesheet" href="https://fonts.googleapis.com/css2?family=Open+Sans:wght@400;600&family=Jura:wght@500&display=swap">
<style>
  :root {
    --backdrop: #161b22;
    --card-light: #f2f2f3;
    --card-dark: #444446;
    --ink: #1c1c1e;
    --accent: #c8202a;
    --white: #ffffff;
  }
  * { margin: 0; padding: 0; box-sizing: border-box; }
  html, body {
    width: 1200px; height: 800px; overflow: hidden;
    background: var(--backdrop);
  }
  .sheet {
    width: 1200px; height: 800px;
    display: flex; flex-direction: column; align-items: center; justify-content: center;
    gap: 32px;
  }
  .card {
    width: 620px; height: 354px;
    position: relative; overflow: hidden;
    box-shadow: 0 6px 18px rgba(0,0,0,.35);
  }
  .brand { display: flex; flex-direction: column; }
  .brand-line { display: flex; align-items: center; gap: 12px; }
  .brand-dot { border-radius: 50%; background: var(--accent); flex: none; }
  .brand-name {
    font-family: "Open Sans", sans-serif; font-weight: 600;
    color: var(--ink); text-transform: uppercase; letter-spacing: 0.04em; line-height: 1;
  }
  .brand-rule { height: 2px; background: var(--accent); }
  .brand-tagline {
    font-family: "Jura", sans-serif; font-weight: 500;
    color: var(--ink); letter-spacing: 0.14em;
  }

  /* front */
  .card-front { background: var(--card-light); display: flex; align-items: center; justify-content: center; }
  .card-front .brand-dot { width: 40px; height: 40px; }
  .card-front .brand-name { font-size: 46px; }
  .card-front .brand-rule { margin: 8px 0 6px 52px; }
  .card-front .brand-tagline { font-size: 20px; margin-left: 52px; }

  /* back */
  .card-back { background: var(--card-dark); }
  .back-band {
    height: 89px; background: var(--card-light);
    display: flex; align-items: center; justify-content: flex-end; padding-right: 34px;
  }
  .card-back .brand-dot { width: 26px; height: 26px; }
  .card-back .brand-name { font-size: 29px; }
  .card-back .brand-rule { margin: 5px 0 4px 38px; }
  .card-back .brand-tagline { font-size: 14px; margin-left: 38px; }

  .back-body { position: absolute; top: 89px; left: 0; right: 0; bottom: 0; }
  .shop-name {
    position: absolute; left: 34px; top: 115px;
    font-family: "Open Sans", sans-serif; font-size: 22px; color: var(--white); letter-spacing: 0.02em;
  }
  .divider {
    position: absolute; left: 292px; top: 64px; width: 2px; height: 140px; background: var(--white);
  }
  .contact-list {
    position: absolute; left: 326px; top: 74px; list-style: none;
    font-family: "Open Sans", sans-serif; font-size: 17px; color: var(--white); line-height: 1.2;
  }
  .contact-item { display: flex; align-items: flex-start; gap: 12px; margin-bottom: 14px; }
  .contact-icon { width: 14px; height: 14px; margin-top: 3px; flex: none; }
</style>
</head>
<body>
<main class="sheet">

  <section class="card card-front" aria-label="Recto de la carte">
    <div class="brand">
      <div class="brand-line">
        <span class="brand-dot"></span>
        <span class="brand-name">Ciel doux</span>
      </div>
      <div class="brand-rule"></div>
      <div class="brand-tagline">lunettes &amp; accessoires</div>
    </div>
  </section>

  <section class="card card-back" aria-label="Verso de la carte">
    <div class="back-band">
      <div class="brand">
        <div class="brand-line">
          <span class="brand-dot"></span>
          <span class="brand-name">Ciel doux</span>
        </div>
        <div class="brand-rule"></div>
        <div class="brand-tagline">lunettes &amp; accessoires</div>
      </div>
    </div>
    <div class="back-body">
      <p class="shop-name">Boutique Ciel doux</p>
      <div class="divider"></div>
      <ul class="contact-list">
        <li class="contact-item">
          <svg class="contact-icon" viewBox="0 0 14 14" aria-hidden="true">
            <rect width="14" height="14" rx="3" fill="#fff"/>
            <path d="M7 2.5a3 3 0 0 0-3 3c0 2.2 3 5.8 3 5.8s3-3.6 3-5.8a3 3 0 0 0-3-3z" fill="#444446"/>
            <circle cx="7" cy="5.5" r="1.1" fill="#fff"/>
          </svg>
          <span>418 Rue Saint-Denis<br>Montreal, Quebec H2X 3K7</span>
        </li>
        <li class="contact-item">
          <svg class="contact-icon" viewBox="0 0 14 14" aria-hidden="true">
            <rect width="14" height="14" rx="3" fill="#fff"/>
            <path d="M4.5 3h1.8l.7 2-1 .8c.5 1.2 1.3 2 2.4 2.5l.8-1 2 .7v1.8c0 .5-.5.9-1 .9C6.6 10.5 3.6 7.5 3.6 4c0-.5.4-1 .9-1z" fill="#444446"/>
          </svg>
          <span>514 555-0142</span>
        </li>
        <li class="contact-item">
          <svg class="contact-icon" viewBox="0 0 14 14" aria-hidden="true">
            <rect width="14" height="14" rx="3" fill="#fff"/>
            <rect x="3" y="4" width="8" height="6" fill="none" stroke="#444446" stroke-width="1.2"/>
            <path d="M3 4l4 3.2L11 4" fill="none" stroke="#444446" stroke-width="1.2"/>
          </svg>
          <span>Cieldoux514@gmail.com</span>
        </li>
      </ul>
    </div>
  </section>

</main>
</body>
</html>
```